Brightway Haul & Repair Services, are a company that offers a 'one stop shop' pre-move clean up a

I have already selected a logo which I would like on the front of the business cards along with phone numbers, web address and email which are:
0419574302
www.brightwayhaul.com.au
brightwayhaulrepair@mailbox.example

On the back of the card I would like to list some of the types of service we offer (clean - move - repairs/maintenance) which are:
CLEAN - windows, gutters, solar panels, driveways/paths, carpets.
MOVE - Small/medium size house/office moves, large item pick-up & delivery, yard clean-up and removal.
General maintenance and repairs.

I would like the blue logo on a gray background.

Thanks

```html
<!DOCTYPE html>
<html lang="en">
<head>
<meta charset="utf-8">
<title>Brightway Haul &amp; Repair Services – Business Card</title>
<link href="https://fonts.googleapis.com/css2?family=Open+Sans:wght@400;600;800&display=swap" rel="stylesheet">
<style>
  :root {
    --page-bg: #e9e7e3;
    --brand-blue: #3a7ac6;
    --brand-blue-dark: #2b5f9e;
    --light-blue: #bcd6f2;
    --silver-light: #f4f4f4;
    --silver-mid: #d2d2d2;
    --silver-dark: #a9a9a9;
    --ink: #2a2a2a;
    --white: #ffffff;
  }
  * { box-sizing: border-box; margin: 0; padding: 0; }
  html, body {
    width: 1200px;
    height: 1001px;
    overflow: hidden;
    background: var(--page-bg);
    font-family: "Open Sans", Arial, sans-serif;
  }
  .sheet {
    width: 1200px;
    height: 1001px;
    display: flex;
    flex-direction: column;
    align-items: center;
    justify-content: center;
    gap: 40px;
  }
  .card {
    width: 720px;
    height: 440px;
    position: relative;
    box-shadow: 0 6px 18px rgba(0,0,0,0.18);
    overflow: hidden;
  }

  /* Back side: services */
  .card-back {
    background: var(--brand-blue);
    color: var(--white);
    display: flex;
  }
  .back-brand {
    width: 50%;
    display: flex;
    align-items: center;
    justify-content: center;
    gap: 12px;
    padding: 0 26px;
  }
  .brand-name {
    font-weight: 800;
    text-transform: uppercase;
    line-height: 1.05;
    letter-spacing: 0.5px;
  }
  .back-brand .brand-name {
    color: var(--light-blue);
    font-size: 27px;
  }
  .divider {
    width: 1px;
    margin: 46px 0;
    background: rgba(255,255,255,0.55);
  }
  .services {
    width: 50%;
    text-align: center;
    padding: 62px 20px 0;
    font-size: 15.5px;
    line-height: 1.6;
  }
  .service-heading {
    font-weight: 600;
    font-size: 17px;
    letter-spacing: 0.5px;
  }
  .service-list { list-style: none; }
  .service-list.inline li { display: inline; margin: 0 6px; }
  .service-group + .service-group { margin-top: 16px; }
  .corner-mark {
    position: absolute;
    right: 22px;
    bottom: 22px;
    width: 30px;
    height: 30px;
    background: var(--white);
  }

  /* Front side: brand and contact */
  .card-front {
    background: radial-gradient(ellipse at 50% 40%, var(--silver-light) 0%, var(--silver-mid) 60%, var(--silver-dark) 100%);
    display: flex;
    flex-direction: column;
    align-items: center;
    justify-content: center;
    gap: 22px;
  }
  .front-brand {
    display: flex;
    align-items: center;
    gap: 16px;
  }
  .front-brand .brand-name {
    color: var(--brand-blue);
    font-size: 44px;
    text-align: left;
  }
  .brand-square {
    width: 22px;
    height: 22px;
    background: var(--brand-blue);
    flex: none;
  }
  .contact {
    display: flex;
    gap: 18px;
    font-size: 12.5px;
    color: var(--ink);
  }
  .contact-label {
    color: var(--brand-blue);
    font-weight: 600;
    margin-right: 4px;
  }
</style>
</head>
<body>
<main class="sheet">

  <section class="card card-back" aria-label="Business card back">
    <div class="back-brand">
      <p class="brand-name">Brightway Haul<br>&amp; Repair Services</p>
    </div>
    <div class="divider"></div>
    <div class="services">
      <div class="service-group">
        <h2 class="service-heading">CLEAN</h2>
        <ul class="service-list inline">
          <li>Windows</li><li>Gutters</li><li>Solar Panels</li><li>Driveways</li><li>Paths</li><li>Carpets</li>
        </ul>
      </div>
      <div class="service-group">
        <h2 class="service-heading">MOVE</h2>
        <ul class="service-list">
          <li>Small/Medium Size House &amp; Office Moves</li>
          <li>Large Item Pick-Up &amp; Delivery</li>
          <li>Yard Clean-Up &amp; Removal.</li>
          <li>General Maintenance &amp; Repairs</li>
        </ul>
      </div>
    </div>
    <span class="corner-mark" aria-hidden="true"></span>
  </section>

  <section class="card card-front" aria-label="Business card front">
    <div class="front-brand">
      <span class="brand-square" aria-hidden="true"></span>
      <p class="brand-name">Brightway Haul<br>&amp; Repair Services</p>
    </div>
    <p class="contact">
      <span><span class="contact-label">Ph.</span>0419574302</span>
      <span><span class="contact-label">Web.</span>www.brightwayhaul.com.au</span>
      <span><span class="contact-label">Mail.</span>brightwayhaulrepair@mailbox.example</span>
    </p>
  </section>

</main>
</body>
</html>
```